Vortapallo Rindelmo needs your help to create a new identity design

We are a basketball team based in Crescentino, Italy.
The official club colors are royal blue and white.
Basically we need a new letterhead and envelope design but not necessary a new logo, but if you want to suggest us a new one we are glad to evaluate it.
If you need any other info please contact us.

Target Market(s)

athletes, their families, other clubs, public institutions, companies

Industry/Entity Type

Club

Other font styles liked:
• the font of our logo or something very similar

Colors
0592cd
ffffff

Requirements
Must have
• our logo, attached to this request; address and other club info such as email address, phone number, facebook page, VAT lot and tax code and obviously our official club colors royal blue and white
Nice to have
• a clear, simple and quite minimal design. A watermark
Should not have
• any other graphic or images such as hoops, ball or court

```html
<!DOCTYPE html>
<html lang="en">
<head>
<meta charset="utf-8">
<title>Vortapallo Rindelmo — Stationery</title>
<link href="https://fonts.googleapis.com/css2?family=Roboto+Condensed:wght@400;700&family=Roboto:wght@300;400&display=swap" rel="stylesheet">
<style>
  :root{
    --bg:#e2e3e5;
    --navy:#0d2f5c;
    --navy-deep:#173a63;
    --royal:#0592cd;
    --paper:#ffffff;
    --paper-soft:#f6f6f6;
    --ink:#1f2f48;
    --muted:#5a6574;
    --rule:#9aa3ad;
  }
  *{box-sizing:border-box;margin:0;padding:0}
  html,body{width:1200px;height:752px;overflow:hidden;background:var(--bg)}
  body{position:relative;font-family:"Roboto",Arial,sans-serif;color:var(--ink)}
  .piece{position:absolute;box-shadow:0 1px 3px rgba(0,0,0,.18)}

  /* club name mark */
  .club-mark{position:absolute;display:flex;align-items:center;gap:4px}
  .club-mark .dot{border-radius:50%;background:var(--royal);flex:none}
  .club-mark .name{font-family:"Roboto Condensed",Arial,sans-serif;font-weight:700;color:var(--navy);text-transform:uppercase;line-height:1.02}
  .club-mark.on-dark .name{color:var(--paper)}

  /* business card front */
  .card-front{left:78px;top:334px;width:294px;height:168px;background:var(--paper)}
  .card-front .club-mark{left:196px;top:30px}
  .card-front .dot{width:10px;height:10px}
  .card-front .name{font-size:12px}
  .person{position:absolute;left:13px;top:88px}
  .person-name{font-family:"Roboto Condensed",Arial,sans-serif;font-weight:700;font-size:10.5px;color:var(--navy)}
  .person-role{font-family:"Roboto Condensed",Arial,sans-serif;font-size:7.5px;color:var(--royal);margin-top:1px}
  .card-front .rule{position:absolute;left:13px;right:15px;top:114px;border-top:1px solid var(--rule)}
  .contact-list{position:absolute;list-style:none;font-size:7px;color:var(--ink)}
  .card-front .contact-list{left:13px;top:120px;line-height:9.6px}
  .contact-list li{display:flex;align-items:center;gap:3px}
  .icon{width:6px;height:6px;flex:none;fill:var(--navy)}
  .card-front .address{position:absolute;right:15px;top:136px;text-align:right;font-size:7px;line-height:9.6px}

  /* business card back */
  .card-back{left:78px;top:534px;width:294px;height:168px;background:var(--navy)}
  .card-back .club-mark{left:50%;top:48px;transform:translateX(-50%)}
  .card-back .dot{width:12px;height:12px}
  .card-back .name{font-size:15px;text-align:left}
  .card-back .web{position:absolute;left:0;right:0;top:146px;text-align:center;color:var(--paper);font-size:6.5px;letter-spacing:2.6px}

  /* letterhead */
  .letterhead{left:422px;top:72px;width:317px;height:445px;background:var(--paper-soft);overflow:hidden}
  .letterhead .watermark{position:absolute;left:70px;top:210px;width:240px;height:250px;border-radius:50%;background:radial-gradient(circle,rgba(220,214,206,.35),rgba(246,246,246,0) 70%)}
  .letterhead .club-mark{left:222px;top:40px}
  .letterhead .dot{width:7px;height:7px}
  .letterhead .name{font-size:8px}
  .salutation{position:absolute;left:28px;top:124px;font-size:7.5px;font-weight:300;color:var(--ink)}
  .letter-body{position:absolute;left:28px;top:146px;width:262px;font-size:4.3px;line-height:6.8px;color:var(--muted)}
  .letter-body p{margin-bottom:6.5px}
  .sign-off{position:absolute;left:28px;top:290px;font-size:4.5px;color:var(--muted)}
  .signature{position:absolute;left:26px;top:306px;width:60px;height:26px;border-radius:40%;background:linear-gradient(90deg,rgba(74,110,180,.25),rgba(74,110,180,.08))}
  .letterhead .rule{position:absolute;left:28px;right:25px;top:391px;border-top:1px solid var(--rule)}
  .letterhead .contact-list{left:28px;top:397px;font-size:4.5px;line-height:6.4px}
  .letterhead .icon{width:4px;height:4px}
  .letterhead .address{position:absolute;right:26px;top:410px;text-align:right;font-size:4.5px;line-height:6.4px;color:var(--muted)}

  /* folder */
  .folder{left:766px;top:44px;width:374px;height:474px;background:var(--navy-deep);overflow:hidden}
  .folder .spine{position:absolute;left:2px;top:0;width:20px;height:100%;background:var(--royal);border-right:2px solid #2a6fae}
  .folder .watermark{position:absolute;left:40px;top:60px;width:360px;height:420px;border-radius:50%;background:radial-gradient(circle,rgba(40,80,130,.55),rgba(23,58,99,0) 70%)}
  .folder .club-mark{left:60px;top:350px}
  .folder .dot{width:16px;height:16px}
  .folder .name{font-size:22px}

  /* compliment envelope */
  .dl-envelope{left:421px;top:550px;width:331px;height:150px;background:var(--paper-soft);overflow:hidden}
  .dl-envelope .watermark{position:absolute;left:210px;top:20px;width:160px;height:150px;border-radius:50%;background:radial-gradient(circle,rgba(220,214,206,.35),rgba(246,246,246,0) 70%)}
  .dl-envelope .club-mark{left:18px;top:20px}
  .dl-envelope .dot{width:6px;height:6px}
  .dl-envelope .name{font-size:6.5px}
  .dl-envelope .address{position:absolute;left:18px;top:124px;font-size:4.5px;line-height:5.8px;color:var(--muted)}

  /* envelope with flap */
  .envelope{left:792px;top:547px;width:331px;height:150px;background:var(--paper);box-shadow:none}
  .envelope .paper{position:absolute;inset:0;background:var(--paper);box-shadow:0 1px 3px rgba(0,0,0,.18)}
  .envelope .flap{position:absolute;left:0;right:0;top:0;height:48px;background:var(--navy);border-radius:0 0 22px 22px}
  .envelope .web{position:absolute;left:0;right:0;top:21px;text-align:center;color:var(--paper);font-size:4.5px;letter-spacing:1px}
  .envelope .club-mark{right:8px;top:10px}
  .envelope .dot{width:6px;height:6px}
  .envelope .name{font-size:6.5px}
</style>
</head>
<body>

<section class="piece card-front" aria-label="Business card front">
  <div class="club-mark"><span class="dot"></span><span class="name">Vortapallo<br>Rindelmo</span></div>
  <div class="person">
    <div class="person-name">MARTA QUELL</div>
    <div class="person-role">CEO/FOUNDER</div>
  </div>
  <div class="rule"></div>
  <ul class="contact-list">
    <li><svg class="icon" viewBox="0 0 10 10"><path d="M2 0l2 2-1 1.5c.6 1.4 1.6 2.4 3 3L7.5 5.5l2 2L8 10C4 9.5.5 6 0 2z"/></svg>555 210 4471</li>
    <li><svg class="icon" viewBox="0 0 10 10"><path d="M0 2h10v6H0z M0 2l5 3.5L10 2" fill="none" stroke="#0d2f5c" stroke-width="1.2"/></svg>name@vortapallo.com</li>
    <li><svg class="icon" viewBox="0 0 10 10"><circle cx="5" cy="5" r="4.3" fill="none" stroke="#0d2f5c" stroke-width="1.2"/><path d="M1 5h8M5 1v8" stroke="#0d2f5c" stroke-width=".9"/></svg>www.vortapallo.com</li>
    <li><svg class="icon" viewBox="0 0 10 10"><rect width="10" height="10" rx="1"/></svg>vortapallo</li>
  </ul>
  <div class="address">12 Linden Row<br>Harbor City 40210</div>
</section>

<section class="piece card-back" aria-label="Business card back">
  <div class="club-mark on-dark"><span class="dot"></span><span class="name">Vortapallo<br>Rindelmo</span></div>
  <div class="web">www.vortapallo.com</div>
</section>

<section class="piece letterhead" aria-label="Letterhead">
  <div class="watermark" role="img" aria-label="Faint club emblem watermark"></div>
  <div class="club-mark"><span class="dot"></span><span class="name">Vortapallo<br>Rindelmo</span></div>
  <p class="salutation">Dear Mr. Dorran,</p>
  <div class="letter-body">
    <p>Thank you for your continued support of our club this season. We are pleased to share the schedule for the coming months, including home games, youth clinics and community events held at the city sports hall. Please find the attached details and contact our office with any questions about tickets or volunteering.</p>
    <p>Our coaching staff has prepared a new training plan for all age groups, with extra sessions on weekends and a focus on teamwork, fitness and fair play. Parents are welcome to attend open practices and meet the coaches after each session to discuss progress and goals for the year.</p>
    <p>We also invite local companies and public institutions to join us as partners. Sponsorship helps cover travel, equipment and facility costs, and gives young athletes the chance to compete at a higher level. Partners receive visibility at home games, on our website and in the season program.</p>
    <p>Thank you again for believing in our players and our community. We look forward to seeing you in the stands and celebrating another great season together.</p>
  </div>
  <p class="sign-off">Sincerely,</p>
  <div class="signature" role="img" aria-label="Handwritten signature"></div>
  <div class="rule"></div>
  <ul class="contact-list">
    <li><svg class="icon" viewBox="0 0 10 10"><path d="M2 0l2 2-1 1.5c.6 1.4 1.6 2.4 3 3L7.5 5.5l2 2L8 10C4 9.5.5 6 0 2z"/></svg>(555) 210-4471</li>
    <li><svg class="icon" viewBox="0 0 10 10"><rect y="2" width="10" height="6"/></svg>marta@vortapallo.com</li>
    <li><svg class="icon" viewBox="0 0 10 10"><circle cx="5" cy="5" r="5"/></svg>www.vortapallo.com</li>
    <li><svg class="icon" viewBox="0 0 10 10"><rect width="10" height="10" rx="1"/></svg>vortapallo</li>
  </ul>
  <div class="address">12 Linden Row<br>Harbor City 40210</div>
</section>

<section class="piece folder" aria-label="Presentation folder">
  <div class="spine"></div>
  <div class="watermark" role="img" aria-label="Large faint club emblem decoration"></div>
  <div class="club-mark on-dark"><span class="dot"></span><span class="name">Vortapallo<br>Rindelmo</span></div>
</section>

<section class="piece dl-envelope" aria-label="Compliment envelope">
  <div class="watermark" role="img" aria-label="Faint club emblem watermark"></div>
  <div class="club-mark"><span class="dot"></span><span class="name">Vortapallo<br>Rindelmo</span></div>
  <div class="address">12 Linden Row<br>Harbor City 40210</div>
</section>

<section class="piece envelope" aria-label="Envelope">
  <div class="paper"></div>
  <div class="flap"></div>
  <div class="web">www.vortapallo.com</div>
  <div class="club-mark on-dark"><span class="dot"></span><span class="name">Vortapallo<br>Rindelmo</span></div>
</section>

</body>
</html>
```